Flyer/Poster to promote Bicycle Race

We need a flyer that promotes a bicycle race in downtown Denver. It need to inspire spectators to come watch and bicycle racers to come race. It benefits the Tall Pines Cycling Club is getting urban kids on bikes; sharing healthy lifestyle and values
. We want the colors to be the colors of the logo - blue & red. Community Partnerships must have their logos on the flyer. Flyer must be able to be printed in 8 1/2 x 11 and 11 x 17

Target Market(s)

Neighborhood residents, athletes, cyclists

Industry/Entity Type

Non Profit

Font styles to use
Serif
Sans Serif

Colors
0592cd
ec1f27

Requirements
Must have
• Sunday, July 31, 2016
• Schedule:
• • Racing starts at 7:00am
• • Fun Ride on the Race Course at 12pm
• • Expo & Festival 10am – 6pm
• A Bike Race for Amateurs and Professionals
• A Bike Race for the young, the old & everyone in the middle.
• Great for spectators. Hang out, watch the action & explore the Festival
• Grab a bite to eat & cheer on the racers as they fly around the corners
• Special activities for kids: Wobblo Course, Maple the Moose & More!!
• Renaldo Vasquez KPLT Music Director and Crosstown Groove Hour host will be onsite!
• Start/Finish/Festival will be on Larkwell St between 9th Ave & 11th Ave
• Net proceeds benefit the Tall Pines Cycling Club dedicated to getting urban youth on bikes; sharing healthy lifestyle and values
• Special thanks to the Harrowgate Foundation for their ongoing support
• LARKWELLSTCRIT.COM

```html
<!DOCTYPE html>
<html lang="en">
<head>
<meta charset="utf-8">
<title>The Larkwell St Crit – Race Flyer</title>
<link href="https://fonts.googleapis.com/css2?family=Oswald:wght@500;700&family=Roboto+Slab:wght@400;800&family=Roboto+Condensed:ital,wght@0,400;0,700;1,400;1,700&display=swap" rel="stylesheet">
<style>
  :root{
    --blue:#0592cd;
    --red:#ec1f27;
    --red-deep:#b8161c;
    --ink:#111111;
    --paper:#ffffff;
  }
  *{margin:0;padding:0;box-sizing:border-box}
  html,body{width:907px;height:1200px;overflow:hidden;background:#ffffff}
  .flyer{position:relative;width:907px;height:1200px;background:var(--paper);overflow:hidden;font-family:"Roboto Condensed",sans-serif}

  /* header */
  .brand{position:absolute;left:28px;top:86px;width:340px;color:var(--ink);font-family:"Oswald",sans-serif;font-weight:700;white-space:nowrap}
  .brand-the{font-size:24px;line-height:1}
  .brand-name{font-size:52px;line-height:1.08;letter-spacing:-.5px}
  .brand-sub{font-size:15px;line-height:1.2;letter-spacing:.3px}
  .headline{position:absolute;left:380px;top:24px;width:500px;text-align:center;white-space:nowrap}
  .headline-top{font-family:"Oswald",sans-serif;font-weight:700;font-size:64px;line-height:1;color:var(--red)}
  .headline-mid{font-family:"Roboto Slab",serif;font-weight:800;font-size:31px;line-height:1.15;color:var(--blue)}
  .headline-end{font-family:"Roboto Slab",serif;font-weight:400;font-size:62px;line-height:1.05;color:var(--ink)}
  .rule-blue{position:absolute;left:0;top:214px;width:907px;height:9px;background:var(--blue)}

  /* photo band */
  .photo-mono{position:absolute;left:0;top:223px;width:404px;height:512px;background:linear-gradient(160deg,#9a9a9a 0%,#4a4a4a 45%,#151515 100%)}
  .photo-color{position:absolute;left:404px;top:223px;width:503px;height:512px;background:linear-gradient(135deg,#e9c9a9 0%,#c9773d 35%,#3d6b2c 70%,#1e2a16 100%)}
  .date{position:absolute;left:40px;top:290px;color:#fff;white-space:nowrap}
  .date-day{font-family:"Oswald",sans-serif;font-weight:500;font-size:70px;line-height:1}
  .date-day sup{font-size:42px;vertical-align:0}
  .date-year{font-family:"Oswald",sans-serif;font-weight:700;font-size:86px;line-height:1.05;color:var(--red);letter-spacing:8px;margin-top:4px}
  .date-weekday{font-family:"Roboto Slab",serif;font-weight:800;font-size:60px;line-height:1;letter-spacing:2px}

  .band-blue{position:absolute;left:420px;top:726px;width:487px;height:9px;background:var(--blue)}
  .band-dark{position:absolute;left:420px;top:735px;width:487px;height:14px;background:var(--ink)}

  /* schedule */
  .schedule-bg{position:absolute;left:0;top:580px;width:480px;height:275px}
  .schedule{position:absolute;left:22px;top:674px;color:#fff;white-space:nowrap}
  .schedule h2{font-family:"Oswald",sans-serif;font-weight:700;font-size:32px;line-height:1.2;letter-spacing:1px;margin-bottom:4px}
  .schedule p{font-style:italic;font-weight:700;font-size:17px;line-height:31px;text-transform:uppercase}
  .schedule p b{font-size:21px}

  /* inset */
  .inset{position:absolute;left:556px;top:586px;width:280px;height:280px}

  /* details */
  .details{position:absolute;top:890px;list-style:none;font-style:italic;font-size:14px;line-height:18px;color:var(--ink)}
  .details li{position:relative;padding-left:22px;margin-bottom:8px}
  .details li::before{content:"";position:absolute;left:2px;top:4px;width:9px;height:9px;border-radius:50%;background:var(--blue)}
  .details li.cont::before{display:none}
  .details li.cont{margin-top:-4px}
  .details-left{left:20px;width:262px}
  .details-right{left:316px;width:268px}

  /* partners */
  .partners{position:absolute;left:605px;top:890px;width:290px}
  .partners h3{font-family:"Roboto Condensed",sans-serif;font-weight:700;font-size:19px;line-height:24px;letter-spacing:.5px;color:var(--ink);text-align:center;margin-bottom:20px}
  .partner-grid{display:grid;grid-template-columns:repeat(4,1fr);grid-auto-rows:36px;row-gap:34px;column-gap:6px;align-items:center;justify-items:center}
  .partner{font-weight:700;font-size:11px;line-height:1.1;text-align:center}
  .partner.wide{grid-column:span 2}
  .partner.red{color:var(--red)}
  .partner.blue{color:var(--blue)}
  .partner.ink{color:var(--ink)}
  .badge{width:32px;height:32px}
  .badge.square-dark{background:#222}
  .badge.circle{border-radius:50%;background:#8a7a4a}
  .badge.square-red{background:var(--red)}
  .badge.square-gold{background:#d8b23a}

  /* footer */
  .foot-blue{position:absolute;left:0;top:1124px;width:907px;height:7px;background:var(--blue)}
  .foot-red{position:absolute;left:0;top:1136px;width:907px;height:7px;background:var(--red-deep)}
  .foot-dark{position:absolute;left:0;top:1150px;width:907px;height:50px;background:var(--ink)}
</style>
</head>
<body>
<main class="flyer">
  <header>
    <div class="brand">
      <div class="brand-the">THE</div>
      <div class="brand-name">LARKWELL ST</div>
      <div class="brand-sub">CRIT · IN MEMORY OF DALE PRUITT</div>
    </div>
    <div class="headline">
      <div class="headline-top">A BIKE RACE FOR</div>
      <div class="headline-mid">THE YOUNG, THE OLD</div>
      <div class="headline-end">&amp; EVERYONE</div>
    </div>
  </header>
  <div class="rule-blue"></div>

  <div class="photo-mono" role="img" aria-label="Black and white photo of a racing cyclist in motion"></div>
  <div class="photo-color" role="img" aria-label="Two road cyclists in helmets and sunglasses racing side by side"></div>

  <div class="date">
    <div class="date-day">31<sup>st</sup> JULY</div>
    <div class="date-year">2016</div>
    <div class="date-weekday">SUNDAY</div>
  </div>

  <div class="band-blue"></div>
  <div class="band-dark"></div>

  <svg class="schedule-bg" viewBox="0 0 480 275" aria-hidden="true">
    <defs>
      <linearGradient id="schedRed" x1="0" y1="0" x2="1" y2="1">
        <stop offset="0" stop-color="#ec1f27"/>
        <stop offset="1" stop-color="#8e1016"/>
      </linearGradient>
    </defs>
    <polygon points="0,35 130,0 480,140 440,270 0,270" fill="url(#schedRed)"/>
    <polygon points="440,270 480,140 480,270" fill="#ffffff"/>
  </svg>
  <div class="schedule">
    <h2>SCHEDULE</h2>
    <p>Racing starts at <b>7:00AM</b></p>
    <p>Fun Ride on the race course at <b>12PM</b></p>
    <p>Expo &amp; Festival <b>10AM – 6PM</b></p>
  </div>

  <svg class="inset" viewBox="0 0 290 290">
    <defs>
      <linearGradient id="insetFill" x1="0" y1="0" x2="0" y2="1">
        <stop offset="0" stop-color="#c9d3dc"/>
        <stop offset=".45" stop-color="#8d5a8f"/>
        <stop offset="1" stop-color="#4a4a52"/>
      </linearGradient>
    </defs>
    <polygon points="87,5 203,5 285,87 285,203 203,285 87,285 5,203 5,87" fill="#ec1f27"/>
    <polygon points="92,16 198,16 274,92 274,198 198,274 92,274 16,198 16,92" fill="#ffffff"/>
    <polygon points="95,23 195,23 267,95 267,195 195,267 95,267 23,195 23,95" fill="#0592cd"/>
    <polygon points="98,30 192,30 260,98 260,192 192,260 98,260 30,192 30,98" fill="url(#insetFill)" role="img" aria-label="A pack of cyclists racing down a street under a memorial banner"/>
  </svg>

  <ul class="details details-left">
    <li>A Bike Race for Amateurs and Professionals</li>
    <li>A Bike Race for the young, the old &amp; everyone in the middle.</li>
    <li>Great for spectators. Hang out, watch the action &amp; explore the Festival</li>
    <li class="cont">Grab a bite to eat &amp; cheer on the racers as they fly around the corners</li>
    <li>Special activities for kids: Wobblo Course, Maple the Moose &amp; More!!</li>
  </ul>
  <ul class="details details-right">
    <li>Renaldo Vasquez KPLT Music Director and Crosstown Groove Hour host will be onsite!</li>
    <li>Start/Finish/Festival will be on Larkwell St between 9th Ave &amp; 11th Ave</li>
    <li>Net proceeds benefit the Tall Pines Cycling Club dedicated to getting urban youth on bikes; sharing healthy lifestyle and values</li>
    <li>Special thanks to the Harrowgate Foundation for their ongoing support</li>
  </ul>

  <section class="partners">
    <h3>OUR PARTNERS</h3>
    <div class="partner-grid">
      <span class="partner red">TALL PINES</span>
      <span class="partner blue">KPLT</span>
      <span class="partner ink wide">SUMMIT VALLEY TV</span>
      <span class="badge square-dark"></span>
      <span class="partner ink">CRESTLINE</span>
      <span class="badge circle"></span>
      <span class="partner ink">RIVERBEND DISTRICT</span>
      <span class="badge square-red"></span>
      <span class="partner blue">KESTREL RACING</span>
      <span class="partner red">ORVANE</span>
      <span class="badge square-gold"></span>
    </div>
  </section>

  <footer>
    <div class="foot-blue"></div>
    <div class="foot-red"></div>
    <div class="foot-dark"></div>
  </footer>
</main>
</body>
</html>
```